CuraNex System Web Page Design

This project is to design 6 pages of a web based medical system for clinics, hospitals, drugs suppliers, general items suppliers, insurance company, laboratories and patients (basically all parties which could be involved in).We want the designs of the browser, button, icon and layout are based on Vex, which is user friendly, looks professional, simple and neat but with powerful functions. We have uploaded few pictures of another system, please do not copy its design because this is not what we are looking for, the pictures are for you to know the elements should be included in our pages. CuraNex web-base system, design 6 pages1. Login PageShould include the following elements-company id with input field-login id with input field-password with input field2. Main Page (Navigation page)Should include the following elements-Appointment-Consultation-Patient-Drugs inventory -General supplies inventory -Laboratory-Suppliers-Insurance-Reports 3. Appointment PageShould include all the the elements in the respective pictures plus the followings-Daily View, Weekly View, Monthly View buttons4. Consultation PageShould include all the the elements in the respective picture5. Patient Page5.1 General information Should include all the the elements in the respective picture5.2 medical history/lab reportsShould include all the the elements in the respective picture plus the followings-Notify patient button-Share report button.
Updated on 28 Nov:
Please stop using Ward Keystone in your designs which is not the name of our system. We have just rename our system to CuraNex, please take note.
We need the system to look professional not playful, do not use too many colors and playful icons.
professional users

```html
<!DOCTYPE html>
<html lang="en">
<head>
<meta charset="utf-8">
<title>CuraNex – Main Navigation</title>
<link href="https://fonts.googleapis.com/css2?family=Montserrat:wght@500;600;700&family=Open+Sans:wght@600&display=swap" rel="stylesheet">
<style>
  :root {
    --navy: #0d3a6e;
    --red: #b8262c;
    --red-deep: #8e1c20;
    --label: #6a6a6a;
    --frame: #e6e6e6;
    --stage: #efeff0;
    --white: #ffffff;
    --footer-text: #555555;
  }
  * { margin: 0; padding: 0; box-sizing: border-box; }
  html, body { width: 1200px; height: 978px; overflow: hidden; }
  body { background: var(--frame); font-family: "Montserrat", sans-serif; }

  .page {
    position: absolute; left: 14px; top: 14px;
    width: 1172px; height: 950px; background: var(--white);
  }

  /* Header */
  .site-header { position: absolute; left: 0; top: 0; width: 100%; height: 129px; background: var(--white); }
  .brand {
    position: absolute; left: 34px; top: 34px;
    display: flex; align-items: center; gap: 14px;
  }
  .brand-mark { width: 40px; height: 40px; border-radius: 50%; background: var(--red); }
  .brand-name { font-size: 50px; font-weight: 700; color: var(--navy); letter-spacing: -0.5px; line-height: 1; }

  .utility-bar {
    position: absolute; right: 0; top: 0; width: 572px; height: 51px;
    background: var(--navy);
    clip-path: polygon(0 0, 100% 0, 100% 100%, 26px 100%);
    display: flex; align-items: center; justify-content: flex-end;
    padding-right: 30px; color: var(--white); font-weight: 600; font-size: 17px;
  }
  .hotline { display: flex; align-items: center; gap: 10px; }
  .divider { width: 1px; height: 28px; background: rgba(255,255,255,.7); margin: 0 20px; }
  .language { display: flex; align-items: center; gap: 8px; }
  .lang-dot { width: 28px; height: 28px; border-radius: 50%; background: #d9dde6; border: 2px solid var(--white); }

  .session-info {
    position: absolute; right: 34px; top: 88px;
    display: flex; gap: 30px; font-size: 16px; font-weight: 500; color: var(--navy);
  }
  .session-item { display: flex; align-items: center; gap: 8px; }
  .session-item b { font-weight: 600; }

  /* Stage */
  .stage {
    position: absolute; left: 0; top: 129px; width: 100%; height: 775px;
    background:
      linear-gradient(155deg, transparent 0 38%, rgba(255,255,255,.55) 38% 52%, transparent 52%),
      linear-gradient(210deg, transparent 0 60%, rgba(255,255,255,.45) 60% 72%, transparent 72%),
      var(--stage);
  }
  .module-grid {
    position: absolute; left: 69px; top: 93px;
    display: grid; grid-template-columns: repeat(3, 332px); grid-auto-rows: 185px; gap: 18px;
  }
  .module-tile {
    background: var(--white); box-shadow: 0 1px 4px rgba(0,0,0,.06);
    display: flex; flex-direction: column; align-items: center;
    padding-top: 24px; text-decoration: none;
  }
  .module-icon { width: 84px; height: 84px; display: flex; align-items: center; justify-content: center; }
  .module-label { margin-top: 24px; font-size: 22px; font-weight: 500; color: var(--label); letter-spacing: .3px; }
  .icon-placeholder { width: 76px; height: 76px; border-radius: 50%; background: var(--navy); opacity: .9; }

  .module-tile.is-active {
    background: linear-gradient(135deg, #c9494c 0%, var(--red) 45%, var(--red-deep) 100%);
  }
  .module-tile.is-active .module-label { color: var(--white); }
  .module-tile.is-active .icon-placeholder { background: var(--white); border-radius: 18px; opacity: 1; }

  /* Footer */
  .site-footer {
    position: absolute; left: 0; bottom: 0; width: 100%; height: 46px;
    display: flex; align-items: center; justify-content: center;
    font-family: "Open Sans", sans-serif; font-weight: 600; font-size: 12px; color: var(--footer-text);
  }
</style>
</head>
<body>
<div class="page">
  <header class="site-header">
    <div class="brand">
      <span class="brand-mark"></span>
      <span class="brand-name">CuraNex</span>
    </div>
    <div class="utility-bar">
      <span class="hotline">
        <svg width="32" height="32" viewBox="0 0 32 32" fill="none" stroke="#fff" stroke-width="2">
          <circle cx="16" cy="16" r="14"/>
          <path d="M11 9c-1 1-2 2-1 5 1 3 4 6 7 8 2 1 4 0 5-1l-2-3-2 1c-2-1-4-3-5-5l1-2z" fill="#fff" stroke="none"/>
        </svg>
        Support Hotline (852) 3904 6120
      </span>
      <span class="divider"></span>
      <span class="language">
        <span class="lang-dot"></span>
        English
        <svg width="14" height="10" viewBox="0 0 14 10" fill="none" stroke="#fff" stroke-width="2.2"><path d="M2 2l5 5 5-5"/></svg>
      </span>
    </div>
    <div class="session-info">
      <span class="session-item">
        <svg width="34" height="32" viewBox="0 0 34 32" fill="none" stroke="#0d3a6e" stroke-width="2">
          <rect x="9" y="10" width="16" height="21"/><rect x="2" y="18" width="7" height="13"/><rect x="25" y="18" width="7" height="13"/>
          <path d="M13 15h2M19 15h2M13 20h2M19 20h2M13 25h2M19 25h2"/>
          <circle cx="17" cy="5" r="4" fill="#b8262c" stroke="none"/>
        </svg>
        Clinic : <b>HARBORVIEW</b>
      </span>
      <span class="session-item">
        <svg width="34" height="32" viewBox="0 0 34 32" fill="none" stroke="#0d3a6e" stroke-width="2">
          <path d="M14 4v8a6 6 0 0012 0V4"/><path d="M20 18v5a6 6 0 01-12 0"/><circle cx="6" cy="24" r="3"/>
          <circle cx="24" cy="6" r="4" fill="#b8262c" stroke="none"/>
        </svg>
        Doctor : <b>DEMO</b>
      </span>
    </div>
  </header>

  <main class="stage">
    <nav class="module-grid">
      <a class="module-tile" href="#appointment">
        <span class="module-icon">
          <svg width="84" height="84" viewBox="0 0 84 84">
            <rect x="2" y="14" width="80" height="68" rx="6" fill="#0d3a6e"/>
            <rect x="2" y="20" width="80" height="4" fill="#fff"/>
            <rect x="20" y="4" width="5" height="20" fill="#0d3a6e"/><rect x="59" y="4" width="5" height="20" fill="#0d3a6e"/>
            <path d="M37 38h10v10h10v10H47v10H37V58H27V48h10z" fill="#fff"/>
          </svg>
        </span>
        <span class="module-label">APPOINTMENT</span>
      </a>
      <a class="module-tile" href="#consultation">
        <span class="module-icon"><span class="icon-placeholder" role="img" aria-label="Consultation icon: doctor with speech bubble"></span></span>
        <span class="module-label">CONSULTATION</span>
      </a>
      <a class="module-tile" href="#patient">
        <span class="module-icon"><span class="icon-placeholder" role="img" aria-label="Patient icon: person figure"></span></span>
        <span class="module-label">PATIENT</span>
      </a>
      <a class="module-tile" href="#drugs">
        <span class="module-icon">
          <svg width="84" height="84" viewBox="0 0 84 84">
            <path d="M60 30l18-24 4 3-18 24z" fill="#0d3a6e"/>
            <path d="M4 36h76c0 18-12 30-28 32H32C16 66 4 54 4 36z" fill="#0d3a6e"/>
            <rect x="18" y="70" width="48" height="8" rx="3" fill="#0d3a6e"/>
            <text x="36" y="60" fill="#fff" font-family="Montserrat, sans-serif" font-weight="700" font-size="18">Rx</text>
          </svg>
        </span>
        <span class="module-label">DRUGS INVENTORY</span>
      </a>
      <a class="module-tile" href="#supplies">
        <span class="module-icon">
          <svg width="84" height="84" viewBox="0 0 84 84">
            <rect x="12" y="2" width="52" height="14" rx="2" fill="#0d3a6e"/>
            <path d="M17 6v6M22 6v6M27 6v6M32 6v6M37 6v6M42 6v6M47 6v6M52 6v6M57 6v6" stroke="#fff" stroke-width="2"/>
            <rect x="14" y="18" width="48" height="64" rx="4" fill="#0d3a6e"/>
            <path d="M34 32h8v8h8v8h-8v8h-8v-8h-8v-8h8z" fill="#fff"/>
            <circle cx="66" cy="70" r="11" fill="#0d3a6e" stroke="#fff" stroke-width="3"/>
          </svg>
        </span>
        <span class="module-label">GENERAL SUPPLIES</span>
      </a>
      <a class="module-tile is-active" href="#laboratory" role="img" aria-label="Laboratory tile with photo of lab equipment in red tones">
        <span class="module-icon"><span class="icon-placeholder" role="img" aria-label="Laboratory icon: microscope"></span></span>
        <span class="module-label">LABORATORY</span>
      </a>
      <a class="module-tile" href="#suppliers">
        <span class="module-icon"><span class="icon-placeholder" role="img" aria-label="Suppliers icon: group of people in a cycle"></span></span>
        <span class="module-label">SUPPLIERS</span>
      </a>
      <a class="module-tile" href="#insurance">
        <span class="module-icon">
          <svg width="84" height="84" viewBox="0 0 84 84">
            <path d="M42 2l36 12v26c0 22-16 36-36 42C22 76 6 62 6 40V14z" fill="#0d3a6e"/>
            <path d="M42 11l27 9v20c0 17-12 28-27 33-15-5-27-16-27-33V20z" fill="#fff"/>
            <path d="M36 26h12v12h12v12H48v12H36V50H24V38h12z" fill="#0d3a6e"/>
          </svg>
        </span>
        <span class="module-label">INSURANCE</span>
      </a>
      <a class="module-tile" href="#reports">
        <span class="module-icon">
          <svg width="84" height="84" viewBox="0 0 84 84">
            <rect x="28" y="8" width="52" height="74" rx="3" fill="none" stroke="#0d3a6e" stroke-width="4"/>
            <rect x="42" y="2" width="24" height="10" rx="2" fill="#0d3a6e"/>
            <path d="M52 26h20M52 36h20M52 46h20M52 56h20M52 66h20" stroke="#0d3a6e" stroke-width="4"/>
            <path d="M24 22l22 8v16c0 16-10 24-22 30C12 70 2 62 2 46V30z" fill="#0d3a6e"/>
            <path d="M20 38h8v8h8v8h-8v8h-8v-8h-8v-8h8z" fill="#fff"/>
          </svg>
        </span>
        <span class="module-label">REPORTS</span>
      </a>
    </nav>
  </main>

  <footer class="site-footer">COPYRIGHT© 2018 CURANEX. ALL RIGHTS RESERVED.</footer>
</div>
</body>
</html>
```